Single-sided business card for restaurant bellamonte with new logo made on this site

Business card options with new logo including restaurant name, address, phone number and website. This business card is single-sided only and will be presented at the hostess desk for clients to take. I would like to see options based on a cream card background, a white card background, a yellow card background and a burgundy colored background. It needs to be elegant and traditional.

Target Market(s)

local and international crowd

Industry/Entity Type

restaurant

Contact Information for Business Card

address, website and phone number

Font styles to use
Serif

Colors
EE7325
F08F49
F5BC92
FAE3D3
FDF4ED

Requirements
Must have
• new logo, address, phone number, website
Should not have
• more than three colors

```html
<!DOCTYPE html>
<html lang="es">
<head>
<meta charset="utf-8">
<title>Bellamonte — Business Card</title>
<link href="https://fonts.googleapis.com/css2?family=Crimson+Text:wght@400&display=swap" rel="stylesheet">
<style>
  :root{
    --backdrop:#2b2b2c;
    --card-yellow:#e9a622;
    --card-yellow-light:#f1b62a;
    --leaf-shade:#d4951e;
    --ink-white:#fffaf0;
    --icon-brown:#3b1d0e;
  }
  *{box-sizing:border-box;margin:0;padding:0}
  html,body{width:1200px;height:900px;overflow:hidden}
  body{background:var(--backdrop);position:relative;font-family:"Crimson Text",Georgia,serif}
  .business-card{
    position:absolute;left:100px;top:165px;width:1000px;height:570px;
    border-radius:42px;overflow:hidden;
    background:linear-gradient(110deg,var(--card-yellow) 0%,var(--card-yellow) 55%,var(--card-yellow-light) 100%);
    box-shadow:0 18px 40px rgba(0,0,0,.45);
  }
  .leaf-decoration{
    position:absolute;right:0;top:0;width:620px;height:570px;
    background:radial-gradient(ellipse at 75% 55%,rgba(200,135,20,.55) 0%,rgba(212,149,30,.35) 45%,rgba(233,166,34,0) 75%);
  }
  .brand{
    position:absolute;left:110px;top:150px;width:240px;
    display:flex;flex-direction:column;align-items:center;color:var(--ink-white);
  }
  .brand-square{width:130px;height:130px;background:var(--ink-white);margin-bottom:26px}
  .brand-name{font-size:36px;font-weight:400;letter-spacing:5px;text-transform:uppercase;line-height:1}
  .brand-since{font-size:11px;letter-spacing:2px;text-transform:uppercase;margin-top:10px}
  .divider{
    position:absolute;left:385px;top:120px;width:1.5px;height:260px;
    background:linear-gradient(to bottom,rgba(255,250,240,0),rgba(255,250,240,.8) 50%,rgba(255,250,240,0));
  }
  .contact-list{position:absolute;left:425px;top:150px;list-style:none;color:var(--ink-white)}
  .contact-item{display:flex;align-items:flex-start;gap:14px;font-size:25px;line-height:1.25;margin-bottom:22px}
  .contact-icon{width:22px;height:22px;flex:none;margin-top:5px;fill:var(--icon-brown)}
</style>
</head>
<body>
  <div class="business-card">
    <div class="leaf-decoration" role="img" aria-label="Faint agave leaf pattern in darker yellow"></div>

    <div class="brand">
      <div class="brand-square"></div>
      <div class="brand-name">Bellamonte</div>
      <div class="brand-since">Desde 1999</div>
    </div>

    <div class="divider"></div>

    <ul class="contact-list">
      <li class="contact-item">
        <svg class="contact-icon" viewBox="0 0 24 24" aria-hidden="true"><path d="M3 8c0-2 3-4 9-4s9 2 9 4v2h-5V8c-2-.8-6-.8-8 0v2H3z"/><path d="M6 12h12l2 8H4z"/></svg>
        <span>958-412-0736</span>
      </li>
      <li class="contact-item">
        <svg class="contact-icon" viewBox="0 0 24 24" aria-hidden="true"><circle cx="12" cy="12" r="10"/><path d="M2 12h20M12 2c3 3 3 17 0 20M12 2c-3 3-3 17 0 20" stroke="#e9a622" stroke-width="1.3" fill="none"/></svg>
        <span>www.bellamonte.com.mx</span>
      </li>
      <li class="contact-item">
        <svg class="contact-icon" viewBox="0 0 24 24" aria-hidden="true"><path d="M12 2a7 7 0 0 0-7 7c0 5 7 13 7 13s7-8 7-13a7 7 0 0 0-7-7zm0 10a3 3 0 1 1 0-6 3 3 0 0 1 0 6z"/></svg>
        <span>Jacaranda 415<br>Bahía Serena, Oaxaca CP 70412</span>
      </li>
    </ul>
  </div>
</body>
</html>
```